Tovek - Business Card Design

Design a modern masculine business card for our business

Target Market(s)

Private Market

Industry/Entity Type

Construction

Contact Information for Business Card

Company Name - Name of Person - Address - email address - contact number

Font styles to use
Serif
Sans Serif

Colors
0094D4
00A9DD
6FCCEA
C7EBF8
E9F6FB
00AB8E
00BBA5
67D7C9
C6EFE9
E9F9F6
F0912C
F2A743
F7CA91
FBE8D2
FDF5EE

Requirements
Must have
• Use company logo provided
Nice to have
• Company Logo

```html
<!DOCTYPE html>
<html lang="en">
<head>
<meta charset="utf-8">
<title>Tovek – Business Card</title>
<link href="https://fonts.googleapis.com/css2?family=Montserrat:wght@800&family=Lato:wght@400;700&display=swap" rel="stylesheet">
<style>
  :root{
    --stage:#3b3b3b;
    --card-dark:#101010;
    --card-light:#ffffff;
    --ink:#141414;
    --orange:#f26f21;
    --white:#ffffff;
  }
  *{margin:0;padding:0;box-sizing:border-box}
  html,body{width:1200px;height:689px;overflow:hidden}
  body{background:var(--stage);position:relative;font-family:'Lato',sans-serif}
  .card{position:absolute;top:194px;width:520px;height:300px;box-shadow:0 14px 30px rgba(0,0,0,.45)}
  .card--front{left:50px;background:var(--card-dark)}
  .card--back{left:630px;background:var(--card-light)}
  .brand{position:absolute;display:flex;align-items:center;gap:12px;
    font-family:'Montserrat',sans-serif;font-weight:800;letter-spacing:2px}
  .brand__mark{width:18px;height:18px;background:var(--orange)}
  .card--front .brand{left:0;right:0;top:0;bottom:0;justify-content:center;
    font-size:64px;color:var(--white)}
  .card--front .brand__mark{width:26px;height:26px}
  .card--back .brand{left:40px;top:128px;font-size:42px;color:var(--ink)}
  .rule{position:absolute;width:2px}
  .rule--orange{left:282px;top:0;height:210px;background:var(--orange)}
  .rule--dark{left:300px;top:60px;height:240px;background:var(--ink)}
  .details{position:absolute;left:318px;top:40px;right:14px}
  .details__name{font-family:'Montserrat',sans-serif;font-weight:800;font-size:23px;color:var(--ink);line-height:1.1}
  .details__role{font-size:14px;color:var(--orange);margin-bottom:14px}
  .contact{list-style:none;font-size:12.5px;color:var(--ink);line-height:1.45}
  .contact li{display:flex;gap:8px;align-items:flex-start;margin-bottom:3px}
  .contact svg{width:12px;height:12px;flex:none;margin-top:3px;fill:var(--orange)}
</style>
</head>
<body>
  <section class="card card--front">
    <div class="brand"><span class="brand__mark"></span>TOVEK</div>
  </section>

  <section class="card card--back">
    <div class="brand"><span class="brand__mark"></span>TOVEK</div>
    <span class="rule rule--orange"></span>
    <span class="rule rule--dark"></span>
    <div class="details">
      <h1 class="details__name">MARCUS HALE</h1>
      <p class="details__role">Founder &amp; CEO</p>
      <ul class="contact">
        <li><svg viewBox="0 0 12 12"><path d="M6 0a4 4 0 0 0-4 4c0 3 4 8 4 8s4-5 4-8a4 4 0 0 0-4-4zm0 5.6A1.6 1.6 0 1 1 6 2.4a1.6 1.6 0 0 1 0 3.2z"/></svg><span>Your Address, City<br>State, Zip 1235</span></li>
        <li><svg viewBox="0 0 12 12"><path d="M2.4 0 4.6 2.6 3.4 4.2a7 7 0 0 0 4.4 4.4l1.6-1.2L12 9.6 10.4 12C4.6 11.6.4 7.4 0 1.6z"/></svg><span>(123) 456-7890</span></li>
        <li><svg viewBox="0 0 12 12"><path d="M3 0h6a1 1 0 0 1 1 1v10a1 1 0 0 1-1 1H3a1 1 0 0 1-1-1V1a1 1 0 0 1 1-1zm.5 1.5v7.5h5V1.5z"/></svg><span>(231) 456-7890</span></li>
        <li><svg viewBox="0 0 12 12"><path d="M3 0h6v3H3zM1 4h10a1 1 0 0 1 1 1v4H10v3H2V9H0V5a1 1 0 0 1 1-1zm2.5 4v2.5h5V8z"/></svg><span>(312) 456-7890</span></li>
        <li><svg viewBox="0 0 12 12"><path d="M0 2h12v8H0zm1 1 5 3.6L11 3z"/></svg><span>info@yourwebsite.com</span></li>
        <li><svg viewBox="0 0 12 12"><path d="M6 0a6 6 0 1 0 0 12A6 6 0 0 0 6 0zm0 1.2c.8.8 1.3 2.4 1.4 4.2H4.6C4.7 3.6 5.2 2 6 1.2zM4.6 6.6h2.8c-.1 1.8-.6 3.4-1.4 4.2-.8-.8-1.3-2.4-1.4-4.2z"/></svg><span>yourwebsite.com</span></li>
      </ul>
    </div>
  </section>
</body>
</html>
```